Design the Marketing Brochure for a service company with Vantage 500 Clients

We need to redesign our marketing brochures to reflect the new service lines we have added in the last few years. We are a professional staffing firm based in Miami, Florida and have a portfolio of clients that include: Coral Meridian, Bluewave Voyage Lines, Patty Palace Corp, Horizon Lens Network Etc. I have attached our current marketing inserts in pdf format. I would like to have 5 inserts displaying our services, process and business lines.

Target Market(s)

Vantage 1000 companies. Within those companies our clients are: CFO's, VP of Finance, Controller, Head of Human Resources, Banking Executives etc. All financial related roles.

Industry/Entity Type

Recruitment

Colors
ec1f27
ffffff
aaaaaa
fece3e
000000

Requirements
Must have
• 5 pages 3 of which we have mots of the content. One page dedicated to " Temporary Staffing" and one page dedicated to our "Banking Division" The brochures should include professional pictures and a well designed layout that looks professional and appealing to an educated client. Our colors are Red, Gray and White.
• Please see our attached brochures and our website at www.kvotalent.example
Nice to have
• Professional pictures of people in the business workplace.
Should not have
• Graphics or cartoons of any kind.

```html
<!DOCTYPE html>
<html lang="en">
<head>
<meta charset="utf-8">
<title>KVO International – Temporary Employees</title>
<link rel="stylesheet" href="https://fonts.googleapis.com/css2?family=Cinzel:wght@600;700&family=Lato:wght@400;700&display=swap">
<style>
  :root {
    --brand-red: #8f0a0a;
    --ink: #2a2a2a;
    --ink-soft: #444444;
    --gray-light: #8c8c8c;
    --gray-dark: #444444;
    --paper: #ffffff;
    --backdrop: #e4e4e4;
  }
  * { box-sizing: border-box; margin: 0; padding: 0; }
  html, body { width: 1200px; height: 1200px; overflow: hidden; background: var(--backdrop); }
  .flyer {
    position: absolute; left: 136px; top: 0; width: 928px; height: 1200px;
    background: var(--paper); font-family: 'Lato', sans-serif; color: var(--ink);
  }
  .hero { position: absolute; left: 0; top: 0; }
  .portrait {
    position: absolute; left: 515px; top: 142px; width: 366px; height: 366px;
    border-radius: 50%; border: 4px solid var(--brand-red); padding: 10px; background: var(--paper);
  }
  .portrait-fill {
    width: 100%; height: 100%; border-radius: 50%;
    background: radial-gradient(circle at 55% 40%, #e9ddd2 0%, #b79c84 35%, #3a3230 75%, #1e1c1c 100%);
  }
  .brand {
    position: absolute; left: 283px; top: 545px; display: flex; align-items: center; gap: 12px;
  }
  .brand-mark { width: 44px; height: 44px; background: var(--brand-red); }
  .brand-name { font-family: 'Lato', sans-serif; font-weight: 700; font-size: 30px; color: var(--gray-dark); letter-spacing: 0.5px; }
  .title {
    position: absolute; left: 0; width: 928px; top: 618px; text-align: center;
    font-family: 'Cinzel', serif; font-weight: 700; font-size: 58px; color: var(--brand-red); letter-spacing: 1px;
  }
  .intro { position: absolute; left: 28px; top: 707px; width: 418px; font-size: 13.2px; line-height: 16.3px; color: var(--ink-soft); letter-spacing: -0.15px; }
  .intro p { margin-bottom: 8px; text-align: justify; }
  .intro strong { color: var(--brand-red); font-weight: 700; }
  .section-head { color: var(--brand-red); font-weight: 700; font-size: 15px; margin-top: 14px; letter-spacing: 0; }
  .section-sub { margin: 6px 0 8px; }
  .needs { list-style: none; }
  .needs li { position: relative; padding-left: 17px; margin-bottom: 2px; }
  .needs li::before { content: ""; position: absolute; left: 5px; top: 6px; width: 4px; height: 4px; border-radius: 50%; background: var(--brand-red); }
  .divider { position: absolute; left: 473px; top: 695px; width: 2px; height: 410px; background: linear-gradient(#ffffff, #dcdcdc 15%, #dcdcdc 85%, #ffffff); }
  .advantages-head { position: absolute; left: 518px; top: 706px; font-size: 17.5px; font-weight: 700; color: var(--brand-red); }
  .advantage { position: absolute; left: 506px; display: flex; align-items: center; gap: 24px; }
  .advantage-icon { width: 50px; height: 50px; flex: none; }
  .advantage-label { font-size: 17.5px; font-weight: 700; color: var(--ink); line-height: 27px; }
  .contact-bar { position: absolute; left: 0; top: 1141px; }
  .contact-items {
    position: absolute; left: 22px; top: 1151px; display: flex; gap: 14px; align-items: flex-start;
    color: #ffffff; font-size: 13.5px; line-height: 17px; white-space: nowrap;
  }
  .contact-item { display: flex; gap: 6px; align-items: flex-start; }
  .contact-item svg { margin-top: 2px; flex: none; }
</style>
</head>
<body>
<main class="flyer">
  <svg class="hero" width="928" height="490" viewBox="0 0 928 490">
    <defs>
      <linearGradient id="deskTone" x1="0" y1="0" x2="1" y2="1">
        <stop offset="0" stop-color="#b9b4ad"/>
        <stop offset="0.45" stop-color="#e9e7e4"/>
        <stop offset="1" stop-color="#cfcdca"/>
      </linearGradient>
    </defs>
    <polygon points="0,0 928,0 928,305 0,480" fill="url(#deskTone)" role="img" aria-label="Photo: a hand on a computer mouse beside a laptop on an office desk"/>
    <polygon points="0,435 424,378 428,423 0,483" fill="var(--brand-red)"/>
  </svg>

  <div class="portrait">
    <div class="portrait-fill" role="img" aria-label="Photo: two businesswomen working together at a desk"></div>
  </div>

  <div class="brand">
    <span class="brand-mark"></span>
    <span class="brand-name">KVO International</span>
  </div>

  <h1 class="title">Temporary Employees</h1>

  <section class="intro">
    <p>At <strong>KVO International</strong>, we know how important it is for you to be able to trust your staffing partner to provide you with a temporary employee on a moment’s notice, especially when you have a tight deadline or are behind on a project.</p>
    <p>We know the type of talent you are looking for. After all, that’s our specialty. With our vast network of best-in-class professionals, we are able to custom fit standout professionals to your specific needs and culture.</p>
    <p>Our Search Consultants are experts at placing temporary employees and high level consultants at a variety of companies from the latest startups to middle market and Vantage 1000 corporations.</p>
    <h2 class="section-head">WHY WOULD YOU NEED A TEMPORARY EMPLOYEE?</h2>
    <p class="section-sub">Common Situations in Today’s Business Environment</p>
    <ul class="needs">
      <li>Do you have a hiring freeze now that prohibits you from hiring someone?</li>
      <li>Do you have a deadline or special project that you need completed?</li>
      <li>Do you need to reduce tax risks associated with 1099 independent contractors?</li>
      <li>Do you want to evaluate a candidate’s skills prior to offering direct employment?</li>
      <li>Do you want to avoid layoffs and bad press?</li>
    </ul>
  </section>

  <div class="divider"></div>

  <h2 class="advantages-head">ADVANTAGES OF TEMPORARY EMPLOYEES</h2>

  <div class="advantage" style="top:747px">
    <svg class="advantage-icon" viewBox="0 0 50 50"><circle cx="25" cy="25" r="25" fill="var(--brand-red)"/><text x="25" y="34" text-anchor="middle" font-family="Lato, sans-serif" font-size="26" font-weight="700" fill="#fff">$</text></svg>
    <span class="advantage-label">Reduce Employment Costs</span>
  </div>
  <div class="advantage" style="top:819px">
    <svg class="advantage-icon" viewBox="0 0 50 50"><circle cx="25" cy="25" r="25" fill="var(--brand-red)"/><g stroke="#fff" stroke-width="1.8" fill="none" stroke-linecap="round"><circle cx="25" cy="24" r="4"/><path d="M25 18v-8M25 30v9M19 24h-8M31 24h8M20 19l-5-5M30 19l5-5"/></g></svg>
    <span class="advantage-label">Staffing Flexibility</span>
  </div>
  <div class="advantage" style="top:893px">
    <svg class="advantage-icon" viewBox="0 0 50 50"><circle cx="25" cy="25" r="25" fill="var(--brand-red)"/><g stroke="#fff" stroke-width="1.8" fill="none"><circle cx="25" cy="25" r="11"/><circle cx="25" cy="22" r="3"/><path d="M19 31c2-4 10-4 12 0"/><path d="M25 8v4M25 38v4M8 25h4M38 25h4" stroke-linecap="round"/></g></svg>
    <span class="advantage-label">Sole-Source Staffing Ability</span>
  </div>
  <div class="advantage" style="top:966px">
    <svg class="advantage-icon" viewBox="0 0 50 50"><circle cx="25" cy="25" r="25" fill="var(--brand-red)"/><g stroke="#fff" stroke-width="1.8" fill="#fff"><path d="M15 15l20 20M35 15L15 35"/><circle cx="14" cy="14" r="3"/><circle cx="36" cy="14" r="3"/><circle cx="14" cy="36" r="3"/><circle cx="36" cy="36" r="3"/><circle cx="25" cy="25" r="6"/></g><text x="25" y="29" text-anchor="middle" font-family="Lato, sans-serif" font-size="10" font-weight="700" fill="var(--brand-red)">$</text></svg>
    <span class="advantage-label">Maintain Budget Controls</span>
  </div>
  <div class="advantage" style="top:1043px">
    <svg class="advantage-icon" viewBox="0 0 50 50"><circle cx="25" cy="25" r="25" fill="var(--brand-red)"/><g stroke="#fff" stroke-width="2" fill="none"><rect x="15" y="21" width="20" height="17" rx="2"/><path d="M19 21v-4a6 6 0 0 1 12 0v4"/></g></svg>
    <span class="advantage-label">Temp-to-Hire Conversions<br>(Try Before You Buy)</span>
  </div>

  <svg class="contact-bar" width="928" height="52" viewBox="0 0 928 52">
    <polygon points="0,0 761,0 741,52 0,52" fill="var(--brand-red)"/>
    <polygon points="779,0 834,0 814,52 759,52" fill="var(--gray-light)"/>
    <polygon points="848,0 906,0 886,52 828,52" fill="var(--gray-dark)"/>
  </svg>
  <div class="contact-items">
    <span class="contact-item"><svg width="12" height="12" viewBox="0 0 12 12"><path d="M2 1l2 0 1 3-1.5 1a7 7 0 0 0 3.5 3.5L8 7l3 1v2c0 1-1 1-1 1A9 9 0 0 1 1 2s0-1 1-1z" fill="#fff"/></svg>(555) 010-4821</span>
    <span class="contact-item"><svg width="14" height="12" viewBox="0 0 14 12"><rect x="1" y="2" width="12" height="9" fill="none" stroke="#fff" stroke-width="1.4"/><path d="M1 2l6 5 6-5" fill="none" stroke="#fff" stroke-width="1.4"/></svg>info@kvotalent.example</span>
    <span class="contact-item"><svg width="13" height="13" viewBox="0 0 13 13"><circle cx="6.5" cy="6.5" r="5.5" fill="none" stroke="#fff" stroke-width="1.3"/><path d="M1 6.5h11M6.5 1c-3 3-3 8 0 11M6.5 1c3 3 3 8 0 11" fill="none" stroke="#fff" stroke-width="1.1"/></svg>www.kvotalent.example</span>
    <span class="contact-item"><svg width="10" height="13" viewBox="0 0 10 13"><path d="M5 0a4.5 4.5 0 0 1 4.5 4.5C9.5 8 5 13 5 13S0.5 8 0.5 4.5A4.5 4.5 0 0 1 5 0z" fill="#fff"/><circle cx="5" cy="4.5" r="1.7" fill="var(--brand-red)"/></svg><span>4310 NW 27 Terrace Suite 210<br>Miami, FL 33100</span></span>
  </div>
</main>
</body>
</html>
```